Social Media Graphics - Harbor Climb REVISED

Create 6-7 individual social media graphics (square size) to encourage folks to join our online course called:

The Lantern Ledger Plan
How to Launch a Multi-Million Business From Scratch
Sign Up Today!

IMPORTANT: Make the largest and most prominent text on the graphic be: How to Launch a Multi-Million Business From Scratch

For the color scheme of the graphics, let's try a blue color palette; make sure the graphics appeal to both men and women

Make sure each graphic contains 1 of the 3 pics attached (crop pic as needed); and make sure one of the graphics is all TEXT only.

Target Market(s)

men and women looking to start a business

Industry/Entity Type

Entrepreneurship

Colors
0054AA
0677BA
7BADD7
CADEEF
E8F1F8

Requirements
Must have
• All the text and use the 3 pics provided; one graphic can be all text; Simple, modern design that's easy to read

```html
<!DOCTYPE html>
<html lang="en">
<head>
<meta charset="UTF-8">
<title>The Lantern Ledger Plan – Social Graphics</title>
<link href="https://fonts.googleapis.com/css2?family=Oswald:wght@500;600;700&family=Roboto+Condensed:wght@700&display=swap" rel="stylesheet">
<style>
  :root {
    --canvas: #8a8a8a;
    --blue-deep: #0054aa;
    --blue-mid: #0677ba;
    --blue-soft: #7badd7;
    --blue-pale: #cadeef;
    --blue-mist: #e8f1f8;
    --navy: #0b2f6b;
    --white: #ffffff;
  }
  * { box-sizing: border-box; margin: 0; padding: 0; }
  html, body { width: 882px; height: 1200px; overflow: hidden; }
  body { background: var(--canvas); position: relative; font-family: "Oswald", sans-serif; }

  .tile {
    position: absolute; width: 296px; height: 296px; overflow: hidden;
    background: linear-gradient(180deg, var(--blue-mid) 0%, var(--blue-deep) 100%);
  }
  .tile--a { left: 134px; top: 132px; }
  .tile--b { left: 452px; top: 132px; }
  .tile--c { left: 134px; top: 450px; }
  .tile--d { left: 452px; top: 450px; }
  .tile--e { left: 134px; top: 768px; }
  .tile--f { left: 452px; top: 768px; }

  .photo { position: absolute; }
  .photo--couple { background: linear-gradient(180deg, #2a4f8a 0%, #3d3a44 55%, #1d2a44 100%); }
  .photo--studio { background: linear-gradient(180deg, #f3f5f8 0%, #c9ccd3 60%, #3a3a44 100%); }

  .brand-band {
    position: absolute; left: 0; right: 0; height: 22px;
    display: flex; align-items: center; justify-content: center;
    font-family: "Roboto Condensed", sans-serif; font-weight: 700;
    font-size: 12px; letter-spacing: 1px; text-transform: uppercase; white-space: nowrap;
    color: var(--white); background: var(--navy);
  }
  .brand-band--light { background: var(--blue-mist); color: var(--blue-deep); }

  .headline {
    position: absolute; color: var(--white); font-weight: 600;
    text-transform: uppercase; line-height: 1.05; text-align: center; white-space: nowrap;
  }
  .headline--base { left: 10px; right: 10px; font-size: 24px; }

  .signup {
    position: absolute; width: 66px; height: 66px; border-radius: 50%;
    background: var(--blue-deep); border: 3px solid var(--white);
    box-shadow: 0 0 0 3px var(--blue-soft);
    display: flex; align-items: center; justify-content: center; text-align: center;
    color: var(--white); font-family: "Roboto Condensed", sans-serif;
    font-weight: 700; font-size: 12px; line-height: 1.1; text-transform: uppercase;
  }
  .signup--small { width: 58px; height: 58px; font-size: 11px; }
  .rule { position: absolute; left: 24px; right: 24px; height: 2px; background: var(--blue-soft); }
</style>
</head>
<body>

  <section class="tile tile--a">
    <div class="photo photo--couple" style="left:0;top:0;width:296px;height:178px" role="img" aria-label="Photo of the course hosts, a man and a woman standing side by side"></div>
    <div class="signup" style="right:16px;top:56px">Sign up<br>today!</div>
    <div class="brand-band" style="top:178px">The Lantern Ledger Plan</div>
    <h2 class="headline headline--base" style="top:208px">How to launch a<br>multi-million business<br>from scratch</h2>
  </section>

  <section class="tile tile--b">
    <div class="brand-band brand-band--light" style="top:14px;left:14px;right:120px;font-size:10px;height:18px">The Lantern Ledger Plan</div>
    <h2 class="headline" style="left:14px;top:40px;font-size:30px;text-align:left;line-height:1.05">How to launch a<br>multi-million<br>business<br>from<br>scratch</h2>
    <div class="photo photo--couple" style="left:140px;top:150px;width:156px;height:146px" role="img" aria-label="Photo of the course hosts smiling"></div>
    <div class="signup signup--small" style="right:10px;top:80px">Sign up<br>today!</div>
  </section>

  <section class="tile tile--c">
    <div class="photo photo--couple" style="left:96px;top:0;width:200px;height:176px" role="img" aria-label="Photo of the course hosts, woman in red beside man"></div>
    <div class="signup" style="left:18px;top:22px">Sign up<br>today!</div>
    <div class="brand-band" style="top:176px">The Lantern Ledger Plan</div>
    <h2 class="headline headline--base" style="top:206px">How to launch a<br>multi-million business<br>from scratch</h2>
    <div class="rule" style="top:286px"></div>
  </section>

  <section class="tile tile--d">
    <div class="brand-band brand-band--light" style="top:0;font-size:11px;height:20px">The Lantern Ledger Plan</div>
    <h2 class="headline headline--base" style="top:30px;font-size:24px">How to launch a<br>multi-million business<br>from scratch</h2>
    <div class="photo photo--studio" style="left:96px;top:122px;width:200px;height:174px" role="img" aria-label="Photo of the course hosts standing on a white background"></div>
    <div class="signup" style="left:22px;top:170px">Sign up<br>today!</div>
  </section>

  <section class="tile tile--e">
    <div class="photo photo--studio" style="left:0;top:0;width:296px;height:172px" role="img" aria-label="Photo of the course hosts on a white background"></div>
    <div class="brand-band" style="top:172px;left:30px;right:30px">The Lantern Ledger Plan</div>
    <h2 class="headline headline--base" style="top:200px">How to launch a<br>multi-million business<br>from scratch</h2>
  </section>

  <section class="tile tile--f">
    <div class="brand-band" style="top:14px;left:40px;right:40px">The Lantern Ledger Plan</div>
    <h2 class="headline" style="left:10px;right:10px;top:52px;font-size:38px;font-weight:700;line-height:1.05">How to launch<br>a multi-million<br><span style="font-size:24px;font-weight:600">business from scratch</span></h2>
    <div class="signup" style="left:115px;top:204px">Sign up<br>today!</div>
  </section>

</body>
</html>
```